Modern corporate energy/fuel business need business card design

Business card required for company founder. Korvan Specialised Energy is a Australian based modern energy/fuel provider. We offer specialised solutions to businesses using fossil fuels through renewable energy solutions.

I would like one side with specific information (name, address etc)

The other side to be bold, professional company name & logo. Striking.

Target Market(s)

B2B. Transport, mining, councils, environmentalist,

Industry/Entity Type

Petroleum

Contact Information for Business Card

Name; Oliver Brentham
Position; Director
Email; obrentham@korvanspec.com.au
Address; PO Box 487, Penrith, NSW, 2751
Website; www.korvanspec.com.au

Colors

Designer to choose colors to be used in the design.

Requirements
Must have
• Clean, easy to read, professional & strong theme
Should not have
• too many colours, busy layout,

```html
<!DOCTYPE html>
<html lang="en">
<head>
<meta charset="utf-8">
<title>Korvan Specialised Energy – Business Card</title>
<link href="https://fonts.googleapis.com/css2?family=Arimo:wght@400;700&display=swap" rel="stylesheet">
<style>
  :root {
    --navy: #27527a;
    --orange: #f26a1b;
    --orange-soft: #fde0cc;
    --card: #ffffff;
    --backdrop: #e9e6e1;
    --text: #1f4a72;
  }
  * { margin: 0; padding: 0; box-sizing: border-box; }
  html, body { width: 900px; height: 1200px; overflow: hidden; }
  body {
    background: var(--backdrop);
    font-family: "Arimo", Arial, sans-serif;
    color: var(--text);
    position: relative;
  }
  .card {
    position: absolute;
    left: 80px;
    width: 732px;
    height: 428px;
    background: var(--card);
    border-radius: 22px;
    overflow: hidden;
    box-shadow: 0 6px 18px rgba(0,0,0,0.18);
  }
  .card--front { top: 128px; }
  .card--back { top: 646px; }

  .card__band {
    position: absolute; left: 0; right: 0; bottom: 0; height: 14px;
    background: var(--orange);
  }
  .card__accent {
    position: absolute; left: 462px; top: 20px;
    width: 300px; height: 230px;
    border-radius: 50%;
    background: var(--orange-soft);
    opacity: 0.8;
  }

  .brand { position: absolute; display: flex; align-items: center; gap: 14px; color: var(--navy); font-weight: 700; }
  .brand__dot { border-radius: 50%; background: var(--orange); flex: none; }
  .brand__name { display: block; line-height: 1; letter-spacing: 3px; }
  .brand__tag { display: block; line-height: 1; margin-top: 6px; }

  .brand--front { left: 42px; top: 52px; }
  .brand--front .brand__dot { width: 78px; height: 78px; }
  .brand--front .brand__name { font-size: 44px; }
  .brand--front .brand__tag { font-size: 13px; letter-spacing: 4.1px; }

  .brand--back { left: 146px; top: 164px; }
  .brand--back .brand__dot { width: 90px; height: 90px; }
  .brand--back .brand__name { font-size: 52px; }
  .brand--back .brand__tag { font-size: 15px; letter-spacing: 4.4px; }

  .holder { position: absolute; left: 42px; top: 270px; display: flex; align-items: baseline; gap: 12px; }
  .holder__name { font-size: 22px; font-weight: 700; color: var(--navy); }
  .holder__role { font-size: 15px; color: var(--orange); }

  .rule { position: absolute; top: 303px; height: 2px; }
  .rule--left { left: 42px; width: 351px; background: var(--navy); }
  .rule--right { left: 403px; width: 285px; background: var(--orange); }

  .contacts { position: absolute; left: 42px; top: 314px; list-style: none; }
  .contacts li { display: flex; align-items: center; gap: 14px; height: 25px; font-size: 16px; }
  .icon { width: 22px; height: 22px; flex: none; }

  .address { position: absolute; right: 44px; top: 314px; display: flex; align-items: center; gap: 12px; font-size: 16px; height: 25px; }

  .web-strip {
    position: absolute; left: 0; right: 0; top: 378px;
    text-align: center; font-size: 16px; letter-spacing: 11px; color: var(--navy);
  }
</style>
</head>
<body>

<section class="card card--front" aria-label="Front of business card">
  <div class="card__accent" aria-hidden="true"></div>

  <div class="brand brand--front">
    <span class="brand__dot"></span>
    <span>
      <span class="brand__name">KORVAN</span>
      <span class="brand__tag">SPECIALISED ENERGY</span>
    </span>
  </div>

  <div class="holder">
    <span class="holder__name">OLIVER BRENTHAM</span>
    <span class="holder__role">DIRECTOR</span>
  </div>
  <div class="rule rule--left"></div>
  <div class="rule rule--right"></div>

  <ul class="contacts">
    <li>
      <svg class="icon" viewBox="0 0 22 22" aria-hidden="true">
        <circle cx="11" cy="11" r="11" fill="#f26a1b"/>
        <path d="M7 6.5c.6-.6 1.4-.5 1.8.1l1 1.5c.3.5.2 1.1-.2 1.5l-.6.5c.6 1.3 1.6 2.3 2.9 2.9l.5-.6c.4-.4 1-.5 1.5-.2l1.5 1c.6.4.7 1.2.1 1.8-1.3 1.3-3.5 1-5.6-1.1S5.7 7.8 7 6.5z" fill="#fff"/>
      </svg>
      <span>0761 2290 3475</span>
    </li>
    <li>
      <svg class="icon" viewBox="0 0 22 22" aria-hidden="true">
        <circle cx="11" cy="11" r="11" fill="#f26a1b"/>
        <rect x="5.5" y="7" width="11" height="8" rx="1" fill="#fff"/>
        <path d="M5.8 7.4 11 11.4l5.2-4" stroke="#f26a1b" stroke-width="1.2" fill="none"/>
      </svg>
      <span>obrentham@korvanspec.com.au</span>
    </li>
    <li>
      <svg class="icon" viewBox="0 0 22 22" aria-hidden="true">
        <circle cx="11" cy="11" r="11" fill="#f26a1b"/>
        <circle cx="11" cy="11" r="5.5" fill="none" stroke="#fff" stroke-width="1.3"/>
        <ellipse cx="11" cy="11" rx="2.4" ry="5.5" fill="none" stroke="#fff" stroke-width="1.1"/>
        <path d="M5.5 11h11" stroke="#fff" stroke-width="1.1"/>
      </svg>
      <span>www.korvanspec.com.au</span>
    </li>
  </ul>

  <div class="address">
    <span>PO Box 487, Penrith, NSW, 2751</span>
    <svg class="icon" viewBox="0 0 22 22" aria-hidden="true">
      <circle cx="11" cy="11" r="11" fill="#f26a1b"/>
      <path d="M11 5a4 4 0 0 1 4 4c0 3-4 7.5-4 7.5S7 12 7 9a4 4 0 0 1 4-4z" fill="#fff"/>
      <circle cx="11" cy="9" r="1.5" fill="#f26a1b"/>
    </svg>
  </div>

  <div class="card__band"></div>
</section>

<section class="card card--back" aria-label="Back of business card">
  <div class="brand brand--back">
    <span class="brand__dot"></span>
    <span>
      <span class="brand__name">KORVAN</span>
      <span class="brand__tag">SPECIALISED ENERGY</span>
    </span>
  </div>
  <div class="web-strip">WWW.KORVANSPEC.COM.AU</div>
</section>

</body>
</html>
```